Book Cover for Lanterns Beyond the Quiet Tide

I need a book cover for a 6 x 9 paperback titled Lanterns Beyond the Quiet Tide Told by Scholars and Souls Dwelling in the Realm past Our Realm. It has to do with consciousness, the mind, incarnation onto Earth, leaving Earth, and the life in the life after this life. I have an idea I'm providing with this description, but I am open to anything that would be striking and stimulating, whether with a book or not. I am the author, T. Dwight Falmer. I've added another background idea to see if anyone can do something with it and I've increased the budget.

```html
<!DOCTYPE html>
<html lang="en">
<head>
<meta charset="utf-8">
<title>Lanterns Beyond the Quiet Tide — Book Cover</title>
<link href="https://fonts.googleapis.com/css2?family=Figtree:wght@600;700;800&display=swap" rel="stylesheet">
<style>
  :root {
    --page-bg: #ffffff;
    --cover-bg: #000000;
    --title-yellow: #ffdd00;
    --title-green: #8dc63f;
    --subtitle-blue: #00aeef;
    --author-purple: #93489a;
  }
  html, body {
    margin: 0;
    padding: 0;
    width: 1200px;
    height: 1000px;
    overflow: hidden;
    background: var(--page-bg);
  }
  .canvas {
    display: block;
    width: 1200px;
    height: 1000px;
  }
  .cover-board { fill: var(--cover-bg); }
  .cover-text {
    font-family: "Figtree", "Helvetica Neue", Arial, sans-serif;
    text-transform: uppercase;
  }
  .title-main { fill: var(--title-yellow); font-weight: 800; }
  .title-rest { fill: var(--title-green); font-weight: 800; }
  .subtitle { fill: var(--subtitle-blue); font-weight: 700; }
  .author {
    fill: var(--author-purple);
    font-weight: 600;
    text-transform: none;
  }
</style>
</head>
<body>
<svg class="canvas" viewBox="0 0 1200 1000" xmlns="http://www.w3.org/2000/svg" role="img" aria-label="Book cover: Lanterns Beyond the Quiet Tide, told by scholars and souls dwelling in the realm past our realm, by T. Dwight Falmer">
  <rect class="cover-board" x="342" y="108" width="510" height="765" rx="6" ry="6"/>

  <g class="cover-text">
    <text class="title-main" x="366" y="295" font-size="220" textLength="450" lengthAdjust="spacingAndGlyphs">Lant</text>
    <text class="title-main" x="366" y="422" font-size="160" textLength="456" lengthAdjust="spacingAndGlyphs">erns</text>

    <text class="title-rest" x="366" y="515" font-size="98" textLength="458" lengthAdjust="spacingAndGlyphs">Beyond</text>
    <text class="title-rest" x="366" y="595" font-size="92" textLength="458" lengthAdjust="spacingAndGlyphs">The Quiet</text>
    <text class="title-rest" x="366" y="668" font-size="90" textLength="458" lengthAdjust="spacingAndGlyphs">Tide</text>

    <text class="subtitle" x="366" y="720" font-size="49" textLength="456" lengthAdjust="spacingAndGlyphs">Told by Scholars</text>
    <text class="subtitle" x="366" y="771" font-size="48" textLength="458" lengthAdjust="spacingAndGlyphs">And Souls Dwelling</text>
    <text class="subtitle" x="366" y="808" font-size="36" textLength="458" lengthAdjust="spacingAndGlyphs">In the Realm Past Our Realm.</text>

    <text class="author" x="366" y="850" font-size="30" textLength="240" lengthAdjust="spacingAndGlyphs">T. Dwight Falmer</text>
  </g>
</svg>
</body>
</html>
```